Verandel Support Coordination

My new business involves providing support coordination for QWPR participants that live with a primary psychosocial and/or developmental delay disability, including but not limited to:

- Anxiety
- Depression
- Bipolar
- Borderline Personality Disorder
- Schizophrenia
- Psychosis
- Autisim Spectrum Disorder
- Fetal Alcohol Spectrum Disorder
- Cerebral Palsy
- Intellectual Disability
- Acquired Brain Injury
- Down Syndrome
- Spina Bifida

The following is an example of another company
https://tallowmerefx.com/

The are basically 3 types of support we offer
- psychosocial recovery coaching
- support coordination
- specialist support coordination

I have attached a copy of my logo, please utilise this colour scheme for website and business cards.

Target Market(s)

See above

Industry/Entity Type

Health Service

Number of Pages Required

5+ page

Font styles to use
Other font styles liked:
• Arial

Colors

Designer to choose only greyscale colors for use in the design.

```html
<!DOCTYPE html>
<html lang="en">
<head>
<meta charset="utf-8">
<title>Verandel Support Coordination</title>
<link rel="stylesheet" href="https://fonts.googleapis.com/css2?family=Poppins:ital,wght@0,400;0,500;0,600;0,700;1,400&display=swap">
<style>
:root{
  --blue:#0a95d9;
  --green:#82c21f;
  --ink:#333333;
  --muted:#6f6f6f;
  --card-blue:#c8e9f8;
  --card-teal:#dff0f2;
  --card-grey:#e2e2e2;
  --quote-bg:#e8eff8;
  --footer-bg:#f7f7f7;
  --white:#ffffff;
}
*{box-sizing:border-box;margin:0;padding:0}
html,body{width:1200px;height:4231px;overflow:hidden}
body{position:relative;font-family:'Poppins',Arial,sans-serif;color:var(--ink);background:var(--white)}
.abs{position:absolute}
.btn{position:absolute;background:var(--green);color:var(--white);font-size:12px;font-weight:500;display:flex;align-items:center;justify-content:center}
.top-bar{left:0;top:0;width:1200px;height:36px;background:var(--blue);color:var(--white);font-size:12px}
.top-bar .item{position:absolute;top:10px;display:flex;align-items:center;gap:7px}
.site-logo{display:flex;align-items:center;gap:8px;color:var(--blue);font-weight:500}
.site-logo .dot{width:14px;height:14px;border-radius:50%;background:var(--green)}
.nav{position:absolute;top:94px;font-size:12px;color:var(--ink)}
.nav.active{color:var(--blue)}
.social{display:flex;gap:14px}
.social span{width:11px;height:11px;border-radius:50%;background:var(--blue)}
.photo{position:absolute}
h1.hero-title{position:absolute;font-weight:700;color:var(--blue);font-size:43px;line-height:49px}
.hero-text{position:absolute;font-size:12.5px;line-height:21px;color:var(--ink)}
.section-title{position:absolute;left:0;width:1200px;text-align:center;font-weight:600;font-size:32px;color:var(--ink)}
.divider{position:absolute;left:420px;width:360px;height:20px}
.divider::before{content:"";position:absolute;left:0;right:0;top:10px;border-top:1px solid #dcdcdc}
.divider span{position:absolute;left:169px;top:0;width:22px;height:22px;border-radius:50%;background:var(--white);border:2px solid var(--green)}
.section-text{position:absolute;left:0;width:1200px;text-align:center;font-size:12.5px;line-height:20.5px;color:var(--muted)}
.card{position:absolute;top:1100px;width:333px;height:218px;text-align:center}
.card svg{margin-top:22px}
.card h3{font-size:19px;font-weight:500;margin-top:12px}
.card p{font-size:12px;line-height:20.5px;color:var(--muted);margin-top:10px}
.card .more{font-size:12px;margin-top:12px;color:var(--ink)}
.card.teal h3{color:#2aa3a3}
.offer{position:absolute;width:330px}
.offer h4{font-size:19px;font-weight:500}
.offer p{font-size:12px;line-height:20.5px;color:var(--muted);margin-top:10px}
.offer.right{text-align:right}
.offer-icon{position:absolute}
.quote{left:236px;top:3529px;width:728px;height:175px;background:var(--quote-bg);text-align:center}
.quote p{font-style:italic;font-size:12px;line-height:20.5px;color:var(--muted);padding:38px 30px 0}
.quote h5{font-size:18px;font-weight:500;margin-top:18px}
.quote small{display:block;font-size:11.5px;color:var(--muted)}
.footer{left:0;top:3817px;width:1200px;height:414px;background:var(--footer-bg)}
.footer h6{position:absolute;top:98px;font-size:18px;font-weight:500}
.footer .txt{position:absolute;font-size:12px;line-height:20.5px;color:var(--muted)}
.footer ul{position:absolute;top:146px;list-style:none;font-size:12px;color:var(--muted)}
.footer li{height:30.7px}
</style>
</head>
<body>

<header>
  <div class="abs top-bar">
    <div class="item" style="left:88px">
      <svg width="15" height="15" viewBox="0 0 16 16"><path d="M3 1l3 3-2 2c1 2 3 4 5 5l2-2 3 3-2 3C7 15 1 9 1 3z" fill="none" stroke="#fff" stroke-width="1.4"/></svg>+1 408 555 0192</div>
    <div class="item" style="left:233px">
      <svg width="16" height="12" viewBox="0 0 16 12"><rect x="1" y="1" width="14" height="10" fill="none" stroke="#fff" stroke-width="1.3"/><path d="M1 1l7 6 7-6" fill="none" stroke="#fff" stroke-width="1.3"/></svg>hello@verandelsupport.com</div>
    <div class="btn" style="left:975px;top:0;width:138px;height:36px;font-size:12.5px">Appointmnet</div>
  </div>

  <div class="abs site-logo" style="left:92px;top:82px;font-size:24px"><span class="dot"></span>Verandel</div>
  <nav>
    <span class="nav active" style="left:455px">Home</span>
    <span class="nav" style="left:522px">Support Coordination</span>
    <span class="nav" style="left:683px">Planning &amp; Reviews</span>
    <span class="nav" style="left:832px">QWPR</span>
    <span class="nav" style="left:891px">About</span>
  </nav>
  <div class="abs social" style="left:1013px;top:96px"><span></span><span></span><span></span><span></span></div>
</header>

<section class="hero">
  <div class="photo" role="img" aria-label="Woman at a laptop holding her glasses, looking stressed" style="left:0;top:153px;width:1200px;height:617px;background:linear-gradient(90deg,#f4f4f3 0%,#ededeb 40%,#b9b5b0 65%,#d8d6d2 85%,#eeeeec 100%)"></div>
  <h1 class="hero-title" style="left:90px;top:293px">Verandel Support<br>Coordination</h1>
  <p class="hero-text" style="left:90px;top:410px">We providing support coordination for QWPR participants that live with<br>a primary psychosocial and/or developmental delay disability.</p>
  <div class="btn" style="left:89px;top:474px;width:139px;height:35px">Appointmnet</div>
</section>

<section class="welcome">
  <h2 class="section-title" style="top:856px">Welcome to Our Company</h2>
  <div class="divider" style="top:918px"><span></span></div>
  <p class="section-text" style="top:960px">Lorem ipsum dolor sit amet, consectetur adipiscing elit. Morbi congue<br>lacus ut lacinia lacinia. Cras fringilla&nbsp; sed erat eu ornare. Donec mollis mi eleifend<br>posuere vestibulum. Morbi placerat.</p>

  <div class="card" style="left:89px;background:var(--card-blue)">
    <svg width="44" height="50" viewBox="0 0 44 50" fill="none" stroke="#555" stroke-width="1.5"><path d="M10 46V34C4 30 4 18 10 12c6-7 20-7 25 2 3 6 2 12-1 16l3 6h-4v6h-8v6"/><circle cx="22" cy="22" r="6"/></svg>
    <h3>Psychosocial Recovery</h3>
    <p>Lorem ipsum dolor sit amet, consectetur<br>adipiscing elit. Morbi congue</p>
    <div class="more">Learn More &nbsp;&nbsp;›</div>
  </div>
  <div class="card teal" style="left:435px;background:var(--card-teal)">
    <svg width="50" height="50" viewBox="0 0 50 50" fill="none" stroke="#2aa3a3" stroke-width="1.5"><path d="M3 22l9-8 8 3 6-3 8 1 13 8M10 26l10 10c2 2 4 1 5-1l6 4c2 1 4-1 3-3l5 2"/></svg>
    <h3>Support Coordination</h3>
    <p>Lorem ipsum dolor sit amet, consectetur<br>adipiscing elit. Morbi congue</p>
    <div class="more">Learn More &nbsp;&nbsp;›</div>
  </div>
  <div class="card" style="left:781px;background:var(--card-grey)">
    <svg width="50" height="50" viewBox="0 0 50 50" fill="none" stroke="#555" stroke-width="1.5"><circle cx="30" cy="16" r="9"/><path d="M4 40h10l10-6h14c2 0 2 4 0 4H26M14 46h14l16-12"/></svg>
    <h3>Specialist Support</h3>
    <p>Lorem ipsum dolor sit amet, consectetur<br>adipiscing elit. Morbi congue</p>
    <div class="more">Learn More &nbsp;&nbsp;›</div>
  </div>
</section>

<section class="feature-band">
  <div class="abs" style="left:0;top:1505px;width:600px;height:332px;background:var(--blue)"></div>
  <div class="photo" role="img" aria-label="Anxious young woman with glasses, hands at her chin" style="left:100px;top:1436px;width:335px;height:401px;background:linear-gradient(180deg,#a8724e 0%,#d9b49a 45%,#e9d6cc 100%);border-radius:150px 150px 0 0"></div>
  <div class="abs" style="left:600px;top:1505px;width:600px;height:332px;background:var(--green)"></div>
  <h2 class="abs" style="left:703px;top:1580px;color:var(--white);font-size:31px;line-height:37px;font-weight:700">Borderline Personality<br>Disorder</h2>
  <p class="abs" style="left:703px;top:1673px;color:var(--white);font-size:12px;line-height:21px">Lorem ipsum dolor sit amet, consectetur adipiscing elit. Morbi<br>congue&nbsp; lacinia. Cras fringilla&nbsp; sed erat eu ornare. Donec mollis mi<br>eleifend posuere vestibulum. Morbi placerat.</p>
  <div class="abs" style="left:703px;top:1759px;color:var(--white);font-size:12px">Learn More &nbsp;&nbsp;›</div>
</section>

<section class="offers">
  <h2 class="section-title" style="top:1976px">What We Offer</h2>
  <div class="divider" style="top:2042px"><span></span></div>
  <p class="section-text" style="top:2085px">Lorem ipsum dolor sit amet, consectetur adipiscing elit. Morbi congue<br>lacus ut lacinia lacinia. Cras fringilla&nbsp; sed erat eu ornare.</p>

  <svg class="offer-icon" style="left:92px;top:2186px" width="56" height="56" viewBox="0 0 56 56" fill="none" stroke="#333" stroke-width="1.5"><path d="M6 50V24l6-10 4 6v14M50 50V24l-6-10-4 6v14M28 40l-10-10c-4-4 2-10 6-6l4 4 4-4c4-4 10 2 6 6z"/></svg>
  <div class="offer" style="left:177px;top:2186px"><h4>Anxiety</h4><p>Lorem ipsum dolor sit amet, consectetur<br>adipiscing elit. Morbi congue</p></div>
  <svg class="offer-icon" style="left:92px;top:2338px" width="56" height="56" viewBox="0 0 56 56" fill="none" stroke="#333" stroke-width="1.5"><path d="M4 52L28 10l24 42zM28 10V2h10v6H28M16 32l6 4 6-4 6 4 6-4"/></svg>
  <div class="offer" style="left:177px;top:2338px"><h4>Depression</h4><p>Lorem ipsum dolor sit amet, consectetur<br>adipiscing elit. Morbi congue</p></div>
  <svg class="offer-icon" style="left:92px;top:2489px" width="56" height="56" viewBox="0 0 56 56" fill="none" stroke="#333" stroke-width="1.5"><path d="M16 52V40c-8-4-10-18-2-26 8-8 26-6 30 6l4 12h-6v8h-8v12M24 22h14v10H24z"/></svg>
  <div class="offer" style="left:177px;top:2489px"><h4>Bipolar</h4><p>Lorem ipsum dolor sit amet, consectetur<br>adipiscing elit. Morbi congue</p></div>

  <div class="offer right" style="left:703px;top:2186px"><h4>Borderline Personality Disorder</h4><p>Lorem ipsum dolor sit amet, consectetur<br>adipiscing elit. Morbi congue</p></div>
  <svg class="offer-icon" style="left:1065px;top:2186px" width="56" height="56" viewBox="0 0 56 56" fill="none" stroke="#333" stroke-width="1.5"><path d="M40 52V40c8-4 10-18 2-26-8-8-26-6-30 6l-4 12h6v8h8v12M22 18c6 0 6 12 14 12"/></svg>
  <div class="offer right" style="left:703px;top:2338px"><h4>Schizophrenia</h4><p>Lorem ipsum dolor sit amet, consectetur<br>adipiscing elit. Morbi congue</p></div>
  <svg class="offer-icon" style="left:1065px;top:2338px" width="56" height="56" viewBox="0 0 56 56" fill="none" stroke="#333" stroke-width="1.5"><circle cx="24" cy="24" r="16"/><circle cx="24" cy="24" r="9"/><path d="M36 36l14 14"/></svg>
  <div class="offer right" style="left:703px;top:2489px"><h4>Psychosis</h4><p>Lorem ipsum dolor sit amet, consectetur<br>adipiscing elit. Morbi congue</p></div>
  <svg class="offer-icon" style="left:1065px;top:2489px" width="56" height="56" viewBox="0 0 56 56" fill="none" stroke="#333" stroke-width="1.5"><path d="M28 4l6 10 12-2-4 12 10 8-12 4 2 12-14-6-14 6 2-12-12-4 10-8-4-12 12 2z"/><circle cx="28" cy="30" r="7"/></svg>

  <div class="abs" style="left:476px;top:2266px;width:246px;height:246px;border-radius:50%;border:4px solid var(--green);display:flex;align-items:center;justify-content:center;font-size:30px;font-weight:500;color:var(--blue)">Verandel</div>

  <div class="btn" style="left:527px;top:2640px;width:141px;height:36px">View All</div>
</section>

<section class="hero">
  <div class="photo" role="img" aria-label="Counsellor comforting a distressed young woman on a couch" style="left:0;top:2783px;width:1200px;height:617px;background:linear-gradient(90deg,#f5f5f4 0%,#efefed 45%,#c9b8a8 68%,#8f95a8 85%,#e4e4e2 100%)"></div>
  <h1 class="hero-title" style="left:97px;top:2965px">Autisim Spectrum<br>Disorder</h1>
  <p class="hero-text" style="left:97px;top:3082px">We providing support coordination for QWPR participants that live with<br>a primary psychosocial and/or developmental delay disability.</p>
  <div class="btn" style="left:97px;top:3141px;width:139px;height:35px">Appointmnet</div>
</section>

<section class="testimonial">
  <div class="abs quote">
    <p>Lorem ipsum dolor sit amet, consectetur adipiscing elit. Morbi congue&nbsp; lacus ut lacinia lacinia. Cras fringilla<br>sed erat eu ornare. Donec mollis mi eleifend posuere vestibulum. Morbi placerat. , enim eu fermentum dictum,<br>erat elit condimentum sapien, vestibulum scelerisque lorem eros in nulla.</p>
    <h5>Name Here</h5>
    <small>Psychologist</small>
  </div>
  <div class="abs" style="left:583px;top:3509px;width:34px;height:34px;border-radius:50%;background:var(--white);border:2px solid var(--green)"></div>
  <div class="abs" style="left:576px;top:3732px;display:flex;gap:14px">
    <span style="width:6px;height:6px;border-radius:50%;background:var(--blue)"></span>
    <span style="width:6px;height:6px;border-radius:50%;background:#bbb"></span>
    <span style="width:6px;height:6px;border-radius:50%;background:#bbb"></span>
  </div>
</section>

<footer class="abs footer">
  <div class="abs site-logo" style="left:109px;top:64px;font-size:24px"><span class="dot"></span>Verandel</div>
  <p class="txt" style="left:107px;top:146px">Lorem ipsum dolor sit amet, consectetur<br>adipiscing elit. Morbi congu us ut lacinia<br>lacinia. Cras fringilla&nbsp; sed erat eu ornare.<br>Donec mollis mi eleifend posuere</p>
  <div class="abs social" style="left:107px;top:264px"><span></span><span></span><span></span><span></span></div>
  <p class="txt" style="left:107px;top:318px">© 2020 Verandel Support Coordination</p>

  <h6 style="left:402px">Address</h6>
  <svg class="abs" style="left:398px;top:148px" width="18" height="22" viewBox="0 0 18 22" fill="none" stroke="var(--blue)" stroke-width="1.4"><path d="M9 21s7-7 7-12A7 7 0 002 9c0 5 7 12 7 12z"/><circle cx="9" cy="9" r="2.5"/></svg>
  <p class="txt" style="left:430px;top:146px">Unit 4 Harwell Close,<br>Marlow Road, Eastbury<br>Fenwick,</p>
  <svg class="abs" style="left:398px;top:224px" width="18" height="18" viewBox="0 0 16 16" fill="none" stroke="var(--blue)" stroke-width="1.4"><path d="M3 1l3 3-2 2c1 2 3 4 5 5l2-2 3 3-2 3C7 15 1 9 1 3z"/></svg>
  <p class="txt" style="left:430px;top:222px">1408 552190</p>
  <svg class="abs" style="left:398px;top:252px" width="18" height="13" viewBox="0 0 16 12" fill="none" stroke="var(--blue)" stroke-width="1.3"><rect x="1" y="1" width="14" height="10"/><path d="M1 1l7 6 7-6"/></svg>
  <p class="txt" style="left:430px;top:248px;color:var(--blue)">info@verandelsupport.com</p>

  <h6 style="left:666px">Our Services</h6>
  <ul style="left:666px">
    <li>- Anxiety</li><li>- Depression</li><li>- Bipolar</li><li>- Borderline Personality Disorder</li><li>- Schizophrenia</li><li>- Psychosis</li><li>- Autisim Spectrum Disorder</li>
  </ul>
  <ul style="left:911px">
    <li>- Fetal Alcohol Spectrum Disorder</li><li>- Cerebral Palsy</li><li>- Intellectual Disability</li><li>- Acquired Brain Injury</li><li>- Down Syndrome</li><li>- Spina Bifida</li>
  </ul>
</footer>

</body>
</html>
```